" Nossa empresa faz atendimentos médicos especializados no tratamento da dor de muito difícil controle sejam estas dores decorrentes de uma cirurgia na coluna, dor do câncer ou qualquer outra. Apartir de uma consulta formulamos modelos de tratamentos com medicamentos associados a técnicas minimamente invasivas para controle das diferentes tipo de dor que os pacientes nos trazem. Somos especialistas em tratamento de dor e utilizamos além de atendimento clínico diversas técnicas de cirurgias modernas para alívio da dor do paciente Uma das técnicas mais modernas e utilizadas são as técnicas de neuromodulação da dor onde atravéz de microchips ou micro eletrodos implantados no corpo do paciente conseguimos bloquear os estímulos neurológicos que levam a informação de dor Fazemos também muito procedimentos chamados minimamente invasivos onde através destas técnicas com mínimo agressão conseguimos alivar as dores dos pacientes "

```html
<!DOCTYPE html>
<html lang="pt-BR">
<head>
<meta charset="UTF-8">
<title>Crachá – Clínica Alívio Pleno</title>
<link href="https://fonts.googleapis.com/css2?family=Roboto:wght@400;700;900&display=swap" rel="stylesheet">
<style>
  :root {
    --brand-blue: #1f4fb5;
    --brand-green: #14a27c;
    --card-white: #ffffff;
    --page-bg: #eef0f2;
    --text-light: #ffffff;
    --rule-light: rgba(255,255,255,0.75);
  }
  * { margin: 0; padding: 0; box-sizing: border-box; }
  html, body { width: 1200px; height: 1200px; overflow: hidden; }
  body {
    background: var(--page-bg);
    font-family: "Roboto", Arial, sans-serif;
    position: relative;
  }
  .badge {
    position: absolute;
    left: 140px;
    top: 482px;
    width: 920px;
    height: 236px;
    background: var(--card-white);
    border-radius: 0 64px 0 64px;
    overflow: hidden;
    box-shadow: 0 6px 18px rgba(0,0,0,0.18);
    display: flex;
  }
  .badge__info {
    width: 436px;
    height: 100%;
    background: var(--brand-blue);
    color: var(--text-light);
    padding: 22px 30px 0 80px;
  }
  .badge__accent {
    width: 9px;
    height: 100%;
    margin-left: 10px;
    background: var(--brand-green);
  }
  .holder-name {
    font-size: 27px;
    font-weight: 700;
    line-height: 1.1;
    padding-bottom: 6px;
    border-bottom: 1.5px solid var(--rule-light);
    width: 250px;
  }
  .holder-role {
    font-size: 16px;
    font-weight: 700;
    margin-top: 10px;
  }
  .booking-title {
    font-size: 15px;
    font-weight: 700;
    margin-top: 22px;
    letter-spacing: 0.2px;
  }
  .contact-row {
    display: flex;
    align-items: center;
    gap: 14px;
    margin-top: 8px;
    margin-left: -6px;
  }
  .contact-row svg { width: 22px; height: 22px; flex: none; }
  .contact-lines { font-size: 15px; font-weight: 700; line-height: 1.2; }
  .contact-lines--web { font-size: 14px; font-weight: 400; }
  .contact-lines--web strong { font-weight: 700; }
  .contact-row--web { margin-top: 16px; }
  .badge__brand {
    flex: 1;
    display: flex;
    align-items: center;
    justify-content: center;
    gap: 18px;
    padding-right: 20px;
  }
  .brand-dot {
    width: 54px;
    height: 54px;
    border-radius: 50%;
    background: var(--brand-green);
    flex: none;
  }
  .brand-name {
    font-size: 38px;
    font-weight: 900;
    color: var(--brand-blue);
    line-height: 1.05;
    text-transform: uppercase;
  }
</style>
</head>
<body>
  <section class="badge">
    <div class="badge__info">
      <h1 class="holder-name">Nome Sobrenome</h1>
      <p class="holder-role">Cargo Nome</p>
      <p class="booking-title">CENTRAL DE MARCAÇÕES</p>
      <div class="contact-row">
        <svg viewBox="0 0 24 24" aria-hidden="true">
          <path fill="#fff" d="M6.6 10.8a15.1 15.1 0 0 0 6.6 6.6l2.2-2.2c.3-.3.7-.4 1-.2 1.1.4 2.3.6 3.6.6.6 0 1 .4 1 1V20c0 .6-.4 1-1 1A17 17 0 0 1 3 4c0-.6.4-1 1-1h3.5c.6 0 1 .4 1 1 0 1.3.2 2.5.6 3.6.1.3 0 .7-.2 1z"/>
        </svg>
        <div class="contact-lines">00 90000 0000<br>00 0000 0000</div>
      </div>
      <div class="contact-row contact-row--web">
        <svg viewBox="0 0 24 24" aria-hidden="true">
          <circle cx="12" cy="12" r="9" fill="none" stroke="#fff" stroke-width="2"/>
          <ellipse cx="12" cy="12" rx="4" ry="9" fill="none" stroke="#fff" stroke-width="1.6"/>
          <line x1="3" y1="12" x2="21" y2="12" stroke="#fff" stroke-width="1.6"/>
        </svg>
        <div class="contact-lines contact-lines--web">contato@site.com.br<br><strong>www.site.com.br</strong></div>
      </div>
    </div>
    <div class="badge__accent"></div>
    <div class="badge__brand">
      <span class="brand-dot"></span>
      <span class="brand-name">Clínica<br>Alívio Pleno</span>
    </div>
  </section>
</body>
</html>
```